Start-up Cleaning Business Needs Professional Business Cards

Marisol's Butler Tidying, LLC, is a start-up business based in the Northern Virginia suburbs of Washington, DC. MBT provides cleaning and housekeeping services for homes and offices. We have three core values:

1. We are personal. We value knowing and being known by our customers and each other. If you want nameless, faceless service, you should choose another provider. We put "personal" at the front of the list, because it is most important to us; the design we choose will convey this value.

2. Like a hotel concierge, we are professional in attitude, posture, communication and processes.

3. Like a hotel concierge, we solve problems with a can-do attitude and never make excuses.

Our uniforms are khaki pants with pink polo shirts.

Our logo is attached. There are other symbols, not represented in our logo, that may convey our values well, such as a top hat and bow tie, magnifying glass, desk bell, etc.

Please include fields for an individual's name and title, office phone number, mobile phone number, email address and website address (www.marisolsbutlertidying-example.com).

Standard U.S. size: 2" x 3.5"
Updates

I should have mentioned that the purpose of all our advertising - business cards included - is to motivate potential customers to call or email to arrange a free in-home estimate.

```html
<!DOCTYPE html>
<html lang="en">
<head>
<meta charset="utf-8">
<title>Marisol's Butler Tidying – Business Cards</title>
<link href="https://fonts.googleapis.com/css2?family=Annie+Use+Your+Telescope&display=swap" rel="stylesheet">
<style>
  :root {
    --page: #e6e6e4;
    --card: #fbf8cf;
    --ink: #2a2a2a;
    --ink-soft: #4a4a4a;
    --pink: #e0457f;
    --hair: #6b3f2a;
    --shadow: rgba(0,0,0,0.18);
  }
  * { box-sizing: border-box; margin: 0; padding: 0; }
  html, body { width: 1200px; height: 900px; overflow: hidden; }
  body {
    background: var(--page);
    font-family: "Annie Use Your Telescope", cursive;
    color: var(--ink);
    position: relative;
  }
  .card {
    position: absolute;
    left: 250px;
    width: 700px;
    height: 400px;
    background: var(--card);
    border-radius: 28px;
    box-shadow: 0 6px 18px var(--shadow);
  }
  .card--info { top: 40px; }
  .card--brand { top: 470px; }

  /* info side */
  .estimate {
    position: absolute;
    left: 48px; top: 52px;
    width: 190px;
    text-align: center;
    font-size: 26px;
    line-height: 1.05;
  }
  .mascot {
    position: absolute;
    background: linear-gradient(160deg, var(--pink) 0%, #f2b6c9 55%, var(--hair) 100%);
    opacity: 0.55;
    border-radius: 14px;
  }
  .card--info .mascot { left: 92px; top: 120px; width: 110px; height: 150px; }
  .brand-name {
    position: absolute;
    text-align: center;
    color: var(--ink);
    line-height: 1;
  }
  .card--info .brand-name { left: 40px; top: 282px; width: 215px; font-size: 28px; }
  .brand-name small { display: block; font-size: 0.55em; margin-top: 4px; }

  .contact {
    position: absolute;
    left: 330px; top: 58px;
  }
  .contact__name { font-size: 38px; letter-spacing: 1px; line-height: 1; }
  .contact__title { font-size: 24px; color: var(--ink-soft); margin-bottom: 8px; }
  .contact__row {
    display: flex; align-items: center; gap: 14px;
    font-size: 32px; line-height: 1.25;
  }
  .contact__row svg { width: 22px; height: 22px; flex: none; }
  .contact__row .spacer { width: 22px; }
  .website {
    position: absolute;
    left: 180px; top: 320px;
    font-size: 34px;
    letter-spacing: 0.5px;
  }

  /* brand side */
  .card--brand .mascot { left: 290px; top: 50px; width: 150px; height: 200px; }
  .card--brand .brand-name { left: 200px; top: 262px; width: 330px; font-size: 54px; }
</style>
</head>
<body>
  <section class="card card--info" aria-label="Business card, contact side">
    <p class="estimate">"Free In-Home Estimate"</p>
    <div class="mascot" role="img" aria-label="Illustration of a housekeeper in a pink uniform mopping"></div>
    <p class="brand-name">Marisol's<small>Butler Tidying</small></p>

    <div class="contact">
      <p class="contact__name">FIRST NAME</p>
      <p class="contact__title">Designation</p>
      <p class="contact__row">
        <svg viewBox="0 0 24 24" aria-hidden="true"><path fill="#2a2a2a" d="M6.6 10.8a15 15 0 0 0 6.6 6.6l2.2-2.2a1 1 0 0 1 1-.25 11.4 11.4 0 0 0 3.6.57 1 1 0 0 1 1 1V20a1 1 0 0 1-1 1A17 17 0 0 1 3 4a1 1 0 0 1 1-1h3.5a1 1 0 0 1 1 1c0 1.25.2 2.45.57 3.57a1 1 0 0 1-.25 1z"/></svg>
        <span>0987-654-321</span>
      </p>
      <p class="contact__row">
        <svg viewBox="0 0 24 24" aria-hidden="true"><rect x="6" y="2" width="12" height="20" rx="2" fill="#2a2a2a"/><rect x="8" y="5" width="8" height="10" fill="#fbf8cf"/><circle cx="12" cy="18.5" r="1.3" fill="#fbf8cf"/></svg>
        <span>123-456-7890</span>
      </p>
      <p class="contact__row">
        <svg viewBox="0 0 24 24" aria-hidden="true"><rect x="2" y="5" width="20" height="14" rx="1.5" fill="#2a2a2a"/><path d="M3 6l9 7 9-7" fill="none" stroke="#fbf8cf" stroke-width="1.6"/></svg>
        <span>name@email.com</span>
      </p>
    </div>

    <p class="website">www.marisolsbutlertidying-example.com</p>
  </section>

  <section class="card card--brand" aria-label="Business card, brand side">
    <div class="mascot" role="img" aria-label="Illustration of a housekeeper in a pink uniform mopping"></div>
    <p class="brand-name">Marisol's<small>Butler Tidying</small></p>
  </section>
</body>
</html>
```